Gift Box design, wine box design-

Please use my logo and colors to come up with a design for a box I can use to send gourmet foods in.
You do not have to use the name, just colors and design ok
you can use the name but maybe a bolder version
Examples attached

Target Market(s)

gourmet food and wine, wine country

```html
<!DOCTYPE html>
<html lang="en">
<head>
<meta charset="utf-8">
<title>Vine Hollow Pantry – Gift Box Panel</title>
<link href="https://fonts.googleapis.com/css2?family=Cinzel:wght@400;500&family=Oswald:wght@400;500&family=Pinyon+Script&display=swap" rel="stylesheet">
<style>
  :root {
    --page: #ffffff;
    --panel-edge: #e9e6df;
    --plum-deep: #24062b;
    --plum: #4a1a52;
    --plum-bright: #5e2766;
    --gold: #c9972f;
    --gold-light: #f1cf72;
    --cream: #f6f3ec;
    --cream-shade: #dcd6cb;
    --wine-ink: #3a1840;
    --berry: #8a3a55;
    --logo-ink: #c7d3e2;
  }
  html, body {
    margin: 0;
    padding: 0;
    width: 1200px;
    height: 1200px;
    overflow: hidden;
    background: var(--page);
  }
  .canvas {
    position: relative;
    width: 1200px;
    height: 1200px;
    background: var(--page);
  }
  .box-panel {
    position: absolute;
    left: 320px;
    top: 50px;
    width: 560px;
    height: 1100px;
    box-sizing: border-box;
    border: 16px solid var(--panel-edge);
    background: linear-gradient(90deg, var(--plum-deep) 0%, var(--plum) 55%, var(--plum-bright) 100%);
  }
  .corner-ornament {
    position: absolute;
    width: 90px;
    height: 120px;
    border-radius: 40px;
    background: radial-gradient(circle, rgba(201,151,47,0.55) 0%, rgba(201,151,47,0) 70%);
  }
  .corner-ornament.top-left { left: 14px; top: 14px; }
  .corner-ornament.top-right { right: 14px; top: 14px; }
  .corner-ornament.bottom-left { left: 14px; bottom: 14px; }
  .corner-ornament.bottom-right { right: 14px; bottom: 14px; }
  .product-label {
    position: absolute;
    left: 44px;
    top: 134px;
    width: 440px;
    height: 800px;
  }
  .label-guarantee { font-family: "Cinzel", serif; font-size: 22px; fill: var(--gold-light); letter-spacing: 1px; }
  .label-brand { font-family: "Oswald", sans-serif; font-size: 28px; font-weight: 400; fill: var(--logo-ink); letter-spacing: 1px; }
  .label-ribbon-text { font-family: "Oswald", sans-serif; font-size: 13px; fill: var(--wine-ink); letter-spacing: 1px; }
  .label-reserve { font-family: "Cinzel", serif; font-size: 18px; fill: var(--berry); }
  .label-script { font-family: "Pinyon Script", cursive; font-size: 32px; fill: var(--berry); }
  .label-wine { font-family: "Oswald", sans-serif; font-size: 120px; font-weight: 500; fill: var(--wine-ink); }
  .label-abv { font-family: "Cinzel", serif; font-size: 15px; fill: var(--berry); }
  .label-quality { font-family: "Pinyon Script", cursive; font-size: 24px; fill: var(--gold); }
</style>
</head>
<body>
<main class="canvas">
  <section class="box-panel">
    <div class="corner-ornament top-left" role="img" aria-label="Gold scroll flourish ornament"></div>
    <div class="corner-ornament top-right" role="img" aria-label="Gold scroll flourish ornament"></div>
    <div class="corner-ornament bottom-left" role="img" aria-label="Gold scroll flourish ornament"></div>
    <div class="corner-ornament bottom-right" role="img" aria-label="Gold scroll flourish ornament"></div>

    <svg class="product-label" viewBox="0 0 440 800" xmlns="http://www.w3.org/2000/svg">
      <defs>
        <linearGradient id="labelPlum" x1="0" y1="0" x2="1" y2="0">
          <stop offset="0" stop-color="#2c0b33"/>
          <stop offset="0.5" stop-color="#4a1f50"/>
          <stop offset="1" stop-color="#2c0b33"/>
        </linearGradient>
        <linearGradient id="bandCream" x1="0" y1="0" x2="1" y2="0">
          <stop offset="0" stop-color="#cfc8bc"/>
          <stop offset="0.3" stop-color="#f8f6f1"/>
          <stop offset="0.75" stop-color="#f4f1ea"/>
          <stop offset="1" stop-color="#cfc8bc"/>
        </linearGradient>
        <linearGradient id="goldEdge" x1="0" y1="0" x2="1" y2="1">
          <stop offset="0" stop-color="#f1cf72"/>
          <stop offset="0.5" stop-color="#a8741f"/>
          <stop offset="1" stop-color="#f1cf72"/>
        </linearGradient>
        <path id="guaranteeArc" d="M95,135 Q220,40 345,135"/>
      </defs>

      <path class="label-frame-outer" d="M10,140 L10,95 L50,95 Q110,10 220,8 Q330,10 390,95 L430,95 L430,140 L430,660 L430,705 L390,705 Q330,790 220,792 Q110,790 50,705 L10,705 L10,660 Z" fill="none" stroke="url(#goldEdge)" stroke-width="5"/>
      <path class="label-frame-inner" d="M22,145 L22,107 L58,107 Q116,26 220,22 Q324,26 382,107 L418,107 L418,145 L418,655 L418,693 L382,693 Q324,774 220,778 Q116,774 58,693 L22,693 L22,655 Z" fill="url(#labelPlum)" stroke="url(#goldEdge)" stroke-width="2"/>

      <text class="label-guarantee"><textPath href="#guaranteeArc" startOffset="50%" text-anchor="middle">100% GUARANTEE</textPath></text>
      <g role="img" aria-label="Small gold crown with flourish">
        <rect x="205" y="118" width="30" height="16" rx="3" fill="var(--gold)"/>
        <rect x="180" y="146" width="80" height="4" rx="2" fill="var(--gold)" opacity="0.6"/>
      </g>

      <text class="label-brand" x="220" y="232" text-anchor="middle">VINE HOLLOW PANTRY</text>

      <rect class="label-band" x="22" y="300" width="396" height="230" fill="url(#bandCream)"/>

      <g class="special-offer-ribbon">
        <path d="M140,290 L300,262 L306,286 L146,314 Z" fill="var(--gold-light)" stroke="var(--gold)" stroke-width="1.5"/>
        <text class="label-ribbon-text" x="223" y="294" text-anchor="middle" transform="rotate(-10 223 290)">SPECIAL OFFER</text>
      </g>

      <text class="label-reserve" x="280" y="345" text-anchor="middle">GRAND RESERVE</text>
      <text class="label-script" x="280" y="382" text-anchor="middle">Original Brand</text>

      <g role="img" aria-label="Grape cluster with vine leaf illustration">
        <rect x="34" y="350" width="116" height="160" rx="50" fill="#4a2552" opacity="0.85"/>
      </g>

      <text class="label-wine" x="170" y="500" textLength="222" lengthAdjust="spacingAndGlyphs">WINE</text>
      <text class="label-abv" x="281" y="522" text-anchor="middle">ALC. 13% BY VOL.</text>

      <text class="label-quality" x="220" y="650" text-anchor="middle">Premium Quality</text>
      <text class="label-quality" x="220" y="680" text-anchor="middle">750ml</text>
      <g role="img" aria-label="Gold laurel wreath">
        <rect x="175" y="688" width="90" height="14" rx="7" fill="var(--gold)" opacity="0.6"/>
      </g>
    </svg>
  </section>
</main>
</body>
</html>
```